Recto Verso Audiology Business Card

Business card with a beautiful design on the back. On the Recto you need the following data Dorvalle Ansel Audiologist Hearing Solutions Hearing Protection Tinnitus Hyperacusis Tel: 0481/27 53 09 Email: On the back, you need something nice like the attached file. The logo "Sola Brisa" can be in the center The colors of the Logo can not be changed If possible stay in the same colors as the logo Another solution is to put the logo on the front and have a nice back (A mosaic of small ears, hearing aids or other ..) Thank you _______________________________________________________________ Visit card On the Recto Dorvalle Ansel Audiologist Hearing Solutions Hearing Protection Tinnitus Hyperacusis Tel: 0481/27 53 09 Email: You can put the logo " Sola Brisa "on the Recto of the Verso The colors of the logo can not be changed. If you put the logo on the back, it must be well integrated. On the Verso I need something in the files. something stylish. It's a visit card for an audiologist. You can get ears of hearing aids if you need. Thanks

Target Market(s)

customers

Contact Information for Business Card

Carte de visite standard ou A6

Font styles to use
Serif
Sans Serif

Colors
33a6d7

Requirements
Must have
• the logo and a stylized background.
Nice to have
• It would be nice to have a back side related to audiology (ears, hearing aids etc.)

```html
<!DOCTYPE html>
<html lang="en">
<head>
<meta charset="utf-8">
<title>Sola Brisa – Audiology Business Card</title>
<link rel="stylesheet" href="https://fonts.googleapis.com/css2?family=Ubuntu:wght@300;400;500;700&display=swap">
<style>
  :root {
    --stage: #e9ecee;
    --teal: #00aabf;
    --teal-soft: #cdeef3;
    --paper: #ffffff;
    --ink: #2e3a40;
    --card-w: 520px;
    --card-h: 804px;
  }
  * { box-sizing: border-box; margin: 0; padding: 0; }
  html, body {
    width: 1200px;
    height: 1040px;
    overflow: hidden;
    background: var(--stage);
    font-family: "Ubuntu", sans-serif;
  }
  .card-set {
    position: relative;
    width: 1200px;
    height: 1040px;
    display: flex;
    justify-content: center;
    align-items: center;
    gap: 40px;
  }
  .card {
    position: relative;
    width: var(--card-w);
    height: var(--card-h);
    overflow: hidden;
    box-shadow: 0 6px 18px rgba(0, 0, 0, 0.12);
  }

  /* Verso: logo over ear pattern */
  .card--verso { background: var(--paper); }
  .ear-pattern {
    position: absolute;
    inset: 0;
    background: linear-gradient(135deg, var(--paper) 0%, var(--teal-soft) 50%, var(--paper) 100%);
  }
  .logo-panel {
    position: absolute;
    left: 130px;
    top: 300px;
    width: 260px;
    height: 170px;
    background: var(--paper);
    display: flex;
    align-items: center;
    justify-content: center;
  }
  .logo-name {
    font-weight: 500;
    font-size: 40px;
    letter-spacing: 2px;
    color: var(--ink);
    text-transform: uppercase;
  }

  /* Recto: contact details */
  .card--recto {
    background: var(--teal);
    color: var(--paper);
    text-align: center;
  }
  .frame {
    position: absolute;
    inset: 22px;
    border: 4px solid var(--paper);
  }
  .contact {
    position: absolute;
    left: 0;
    right: 0;
    top: 200px;
  }
  .contact-name {
    font-weight: 500;
    font-size: 29px;
    margin-bottom: 10px;
  }
  .contact-role {
    font-weight: 300;
    font-size: 19px;
    line-height: 1.4;
  }
  .contact-phone {
    font-weight: 500;
    font-size: 28px;
    letter-spacing: 1px;
    margin-top: 38px;
  }
  .contact-email {
    font-weight: 500;
    font-size: 21px;
    margin-top: 12px;
  }
</style>
</head>
<body>
<main class="card-set">
  <section class="card card--verso">
    <div class="ear-pattern" role="img" aria-label="Repeating pattern of small teal ear and sound-wave icons on white"></div>
    <div class="logo-panel">
      <span class="logo-name">Sola Brisa</span>
    </div>
  </section>

  <section class="card card--recto">
    <div class="frame"></div>
    <div class="contact">
      <p class="contact-name">Dorvalle Ansel</p>
      <p class="contact-role">Audiologist Hearing Solutions</p>
      <p class="contact-role">Hearing Protection Tinnitus Hyperacusis</p>
      <p class="contact-phone">0481 27 53 09</p>
      <p class="contact-email">info@solabrisamedical.com</p>
    </div>
  </section>
</main>
</body>
</html>
```